Automotive eCommerce Business looking for a business card design

Looking for a clean and simple business card design. Our company name is "Harbor Crest Auto" and we are a company specializing in the ecommerce sales of automotive parts, specifically for pick up trucks and large SUVs. Our company colours are red, black, and white.

Feel free to use the logo provided or create a new logo that you seem fit. Looking forward to your creative ideas!

Industry/Entity Type

Automotive

Contact Information for Business Card

We were thinking of a possibly two-sided design featuring just the logo and company name on one side, and personal information on the other side. Single sided designs will be considered as well.

Font styles to use
Serif
Sans Serif
Decorative

Colors
ec1f27
ffffff
000000

Requirements
Must have
• Space for employee's name, title, phone number and email address, along with the company address and website somewhere.

```html
<!DOCTYPE html>
<html lang="en">
<head>
<meta charset="utf-8">
<title>Harbor Crest Auto – Business Card</title>
<link rel="stylesheet" href="https://fonts.googleapis.com/css2?family=Cinzel:wght@500&family=Roboto:wght@400&family=Roboto+Condensed:wght@500&display=swap">
<style>
  :root {
    --backdrop: #1e1e1e;
    --card-white: #f1f1f1;
    --brand-red: #9b1c20;
    --ink: #4a4a4a;
    --ink-strong: #3c3c3c;
    --white: #ffffff;
  }
  * { margin: 0; padding: 0; box-sizing: border-box; }
  html, body { width: 1200px; height: 960px; overflow: hidden; }
  body {
    background: var(--backdrop);
    position: relative;
    font-family: "Roboto", Arial, sans-serif;
  }
  .card {
    position: absolute;
    width: 600px;
    height: 343px;
    box-shadow: 0 3px 8px rgba(0,0,0,0.5);
  }
  .card--front { left: 314px; top: 113px; background: var(--card-white); }
  .card--back  { left: 311px; top: 472px; background: var(--brand-red); }

  .brand-square { position: absolute; }
  .card--front .brand-square {
    left: 82px; top: 34px; width: 94px; height: 94px;
    background: var(--brand-red);
  }
  .card--back .brand-square {
    left: 248px; top: 86px; width: 106px; height: 106px;
    background: var(--card-white);
  }

  .company-name {
    position: absolute;
    font-family: "Cinzel", Georgia, serif;
    font-weight: 500;
    white-space: nowrap;
  }
  .card--front .company-name {
    left: 32px; top: 147px;
    font-size: 20px; color: var(--ink);
  }
  .card--back .company-name {
    left: 0; width: 600px; top: 230px; text-align: center;
    font-size: 24px; color: var(--white);
  }

  .address {
    position: absolute; left: 34px; top: 197px;
    font-size: 14.5px; line-height: 18px; color: var(--ink);
  }
  .contact-list {
    position: absolute; left: 34px; top: 240px;
    list-style: none; font-size: 14.5px; line-height: 19px; color: var(--ink);
  }
  .contact-list li { display: flex; align-items: center; gap: 8px; }
  .contact-icon { width: 15px; height: 15px; fill: var(--brand-red); flex: none; }

  .person {
    position: absolute; right: 38px; top: 234px; text-align: right;
  }
  .person-name {
    font-family: "Roboto Condensed", Arial, sans-serif;
    font-weight: 500; font-size: 21px; color: var(--brand-red); line-height: 24px;
  }
  .person-title {
    font-family: "Roboto Condensed", Arial, sans-serif;
    font-weight: 500; font-size: 15px; color: var(--ink-strong); line-height: 22px;
  }

  .website {
    position: absolute; left: 0; width: 600px; top: 291px; text-align: center;
    font-size: 14px; letter-spacing: 4.6px; color: var(--white);
  }
</style>
</head>
<body>

<section class="card card--front">
  <div class="brand-square"></div>
  <div class="company-name">Harbor Crest Auto Ltd.</div>

  <p class="address">4120 Juniper Ridge Road<br>Fairbanks, Alaska 99709</p>

  <ul class="contact-list">
    <li>
      <svg class="contact-icon" viewBox="0 0 16 16"><path d="M3.5 1.5l2.3 2.8-1.4 1.6c.9 2 2.4 3.5 4.3 4.4l1.6-1.4 2.8 2.3-1.5 2.3C6.9 13.3 2.7 9.1 1.2 3z"/></svg>
      <span>907 555 0148</span>
    </li>
    <li>
      <svg class="contact-icon" viewBox="0 0 16 16"><path d="M4.5 0.5h7v15h-7zM5.8 2v10.5h4.4V2z"/><circle cx="8" cy="13.9" r="0.8" fill="#f1f1f1"/></svg>
      <span>907 555 0173</span>
    </li>
    <li>
      <svg class="contact-icon" viewBox="0 0 16 16"><path d="M4 1h8v4H4zM1 6h14v6h-2.5v3h-9v-3H1zM5 10v3.5h6V10z"/></svg>
      <span>907 555 0196</span>
    </li>
    <li>
      <svg class="contact-icon" viewBox="0 0 16 16"><path d="M1 4h14v9H1z"/><path d="M1.5 4.5L8 9l6.5-4.5" fill="none" stroke="#f1f1f1" stroke-width="1.2"/></svg>
      <span>daniel@harborcrestauto.com</span>
    </li>
  </ul>

  <div class="person">
    <div class="person-name">DANIEL REEVE</div>
    <div class="person-title">CEO/FOUNDER</div>
  </div>
</section>

<section class="card card--back">
  <div class="brand-square"></div>
  <div class="company-name">Harbor Crest Auto Ltd.</div>
  <div class="website">www.harborcrestauto.com</div>
</section>

</body>
</html>
```